Website

I have a client that we built a website for about 10 years ago - https://www.pinloopcards.com.au/

We would like a fresh new design for it that looks more modern. All the elements, info that's on there needs to be the same but the whole design/layout needs to be modernised.

```html
<!DOCTYPE html>
<html lang="en">
<head>
<meta charset="utf-8">
<title>Pinloop Cards — website redesign</title>
<link rel="stylesheet" href="https://fonts.googleapis.com/css2?family=Inter:wght@400;500;600;700&display=swap">
<style>
:root{
  --stage:#d1d1d1;
  --page:#121724;
  --page-2:#0f1420;
  --glow:rgba(120,30,45,.45);
  --card:#1c2130;
  --card-2:#222736;
  --line:#313748;
  --text:#f2f3f6;
  --muted:#a4aaba;
  --dim:#7d8496;
  --red:#c3151e;
  --red-dark:#7a0d14;
  --white:#ffffff;
}
*{box-sizing:border-box;margin:0;padding:0}
html,body{width:1200px;height:927px;overflow:hidden;background:var(--stage)}
body{font-family:"Inter",system-ui,sans-serif;color:var(--text)}
.board{position:absolute;left:0;top:0;width:2184px;height:1687px;transform:scale(.54945);transform-origin:0 0}
.screen{position:absolute;width:993px;overflow:hidden;background:
  radial-gradient(700px 140px at 50% 0,var(--glow),transparent 70%),
  linear-gradient(180deg,#1b1a26 0,var(--page) 120px,var(--page-2) 100%);
  box-shadow:0 10px 30px rgba(0,0,0,.25)}
.screen--home{left:78px;top:78px;height:1304px}
.screen--products{left:1113px;top:78px;height:624px}
.screen--prices{left:1113px;top:745px;height:431px}
.screen--trade{left:1113px;top:1218px;height:391px}

.notice{height:19px;background:linear-gradient(90deg,#3a1a22,#2a1820 50%,#3a1a22);display:flex;align-items:center;justify-content:center;font-size:7.5px;color:#e6e7ec;position:relative}
.notice b{font-weight:600}
.notice .dot{position:absolute;left:80px;width:7px;height:7px;border-radius:50%;background:var(--red)}
.notice .pay{position:absolute;right:83px}
.site-header{height:40px;display:flex;align-items:center;padding:0 83px 0 82px;border-bottom:1px solid rgba(255,255,255,.05);background:rgba(15,18,28,.6)}
.brand{width:74px;height:39px;background:var(--white);display:flex;align-items:center;gap:4px;padding:0 5px}
.brand i{width:7px;height:7px;background:var(--red);flex:none}
.brand span{font-size:9px;font-weight:700;color:var(--red);line-height:1}
.nav{flex:1;display:flex;justify-content:center;gap:18px;font-size:7.5px;color:#d4d6de}
.nav .on{background:#2a2f3d;border:1px solid var(--line);border-radius:10px;padding:4px 7px;margin:-5px 0}
.head-actions{display:flex;gap:6px}
.btn{display:inline-flex;align-items:center;justify-content:center;border-radius:11px;font-size:8px;font-weight:600;padding:0 9px;height:21px;border:1px solid var(--line);background:#1a1e2a;color:var(--text);white-space:nowrap}
.btn--red{background:linear-gradient(90deg,var(--red),#9e1118);border-color:#d2262e;color:#5b0a0f}

.wrap{padding:0 83px 0 82px}
.eyebrow{font-size:6.5px;letter-spacing:.8px;font-weight:600;color:#cfd2db}
h1{font-size:25px;line-height:26px;font-weight:700;letter-spacing:-.4px;margin-top:6px}
h2{font-size:14px;font-weight:600}
h3{font-size:19px;font-weight:700}
.lead{font-size:8.5px;line-height:14px;color:var(--muted)}
.chip{display:inline-flex;align-items:center;height:17px;border-radius:9px;border:1px solid var(--line);padding:0 7px;font-size:6.5px;color:#cfd2db;background:#171b26}
.chip b{font-weight:600;margin-right:3px;color:var(--white)}

.hero{position:absolute;left:82px;top:88px;width:828px;height:220px}
.hero-copy{position:absolute;left:0;top:0;width:430px}
.hero-builder{position:absolute;left:483px;top:0;width:345px;height:118px;border:1px solid var(--line);border-radius:10px;background:#1a1e2a;padding:9px}
.mock{height:77px;border:1px solid #3a3f4e;border-radius:8px;background:linear-gradient(180deg,#2a2d3b,#23263340);position:relative}
.mock .logo{position:absolute;left:8px;top:8px;width:30px;height:30px;border-radius:6px;background:#5b2a33;border:1px solid #8a3a44;font-size:5.5px;color:#f1d6d9;display:flex;align-items:center;justify-content:center}
.mock .bar{position:absolute;left:44px;height:6px;border-radius:3px;background:#5a5f6d}
.hero-calc{position:absolute;left:483px;top:127px;width:345px;height:76px;border:1px solid var(--line);border-radius:10px;background:#1a1e2a;padding:10px 9px}
.hero-calc .go{margin-top:7px;height:19px;border-radius:10px;background:linear-gradient(90deg,var(--red),#3b0f15);font-size:7.5px;color:#5b0a0f;display:flex;align-items:center;justify-content:center;font-weight:600}

.section{position:absolute;left:82px;width:828px}
.feature-grid{display:grid;grid-template-columns:repeat(3,1fr);gap:7px}
.feature{border:1px solid var(--line);border-radius:8px;background:var(--card);padding:9px 8px}
.feature h4{font-size:8px;font-weight:600;margin-bottom:5px}
.feature p{font-size:6.8px;line-height:11px;color:var(--muted)}

.product-grid{display:grid;grid-template-columns:repeat(5,1fr);gap:7px}
.product{height:84px;border:1px solid var(--line);border-radius:8px;background:var(--card-2);padding:9px 7px;display:flex;flex-direction:column}
.product .ico{width:8px;height:7px;border-radius:2px;margin-bottom:6px}
.product h4{font-size:6.8px;font-weight:600;margin-bottom:3px}
.product p{font-size:6px;line-height:9.5px;color:var(--muted);flex:1}
.product .view{align-self:flex-start;font-size:5.8px;color:#cfd2db;border:1px solid var(--line);border-radius:7px;padding:2px 6px;background:#1a1e2a}

.band{position:absolute;left:0;width:993px;background:rgba(10,13,20,.45)}
.clients{display:flex;align-items:center;justify-content:space-between;height:100%;padding:0 83px 0 82px;font-size:7px;color:#cfd2db}
.clients .list{display:flex;gap:5px}

.two-col{display:grid;grid-template-columns:1fr 1fr;gap:9px}
.panel{border:1px solid var(--line);border-radius:8px;background:var(--card);padding:10px 9px}
.panel h4{font-size:9px;font-weight:600;margin-bottom:6px}
.panel p{font-size:7.8px;line-height:13.5px;color:#c7cad4}
.panel a{color:var(--text);text-decoration:underline;font-size:7.5px}

.cta{border:1px solid #5a2a36;border-radius:9px;background:linear-gradient(90deg,#3a1b26,#221a26);height:54px;display:flex;align-items:center;padding:0 11px}
.cta .txt{flex:1}
.cta h4{font-size:11px;font-weight:600}
.cta p{font-size:7.5px;color:var(--muted);margin-top:3px}

.site-footer{position:absolute;left:0;width:993px;bottom:0;border-top:1px solid rgba(255,255,255,.04);background:
  radial-gradient(700px 120px at 50% 100%,rgba(110,25,40,.4),transparent 70%),rgba(10,13,20,.55)}
.footer-cols{position:relative;height:100%;font-size:7.8px;line-height:14.2px;color:#c9ccd5}
.footer-cols .col{position:absolute;top:10px}
.footer-cols h5{font-size:8px;font-weight:600;color:var(--white)}

.page-body{position:absolute;left:83px;width:828px}
.big-box{border:1px solid var(--line);border-radius:10px;background:rgba(28,33,48,.7);padding:10px 9px;font-size:8px;line-height:13.7px;color:#d7dae2}
.big-box .note{margin-top:7px;border:1px solid var(--line);border-radius:9px;padding:8px 9px;font-style:italic;color:#c5c8d2;font-size:7.8px}
.big-box ul{list-style:none;padding-left:13px}
.big-box li::before{content:"• "}
</style>
</head>
<body>
<div class="board">

  <!-- Home -->
  <section class="screen screen--home">
    <div class="notice"><span class="dot"></span><span><b>Notice:</b> PC will close over Christmas / New year. We are back on <b>19th January 2025</b>.</span><span class="pay">Payment Options</span></div>
    <header class="site-header">
      <div class="brand"><i></i><span>Pinloop Cards</span></div>
      <nav class="nav"><span class="on">Home</span><span>Products</span><span>Price list</span><span>Re-sellers / trade info</span><span>FAQs</span><span>Artwork requirements</span><span>Payment</span><span>Contact</span></nav>
      <div class="head-actions"><span class="btn">Login</span><span class="btn btn--red">Build a badge</span></div>
    </header>

    <div class="hero">
      <div class="hero-copy">
        <div class="eyebrow">NAME TAGS AUSTRALIA</div>
        <h1>The best custom name badges for companies &amp; individuals across Australia.</h1>
        <p class="lead" style="margin-top:8px;width:310px">Tailor your name tags to suit your exact requirements with a choice of sizes, colours, fittings and finishes — delivered Australia-wide.</p>
        <div style="display:flex;gap:6px;margin-top:10px"><span class="btn btn--red" style="width:121px">Design &amp; order your badge</span><span class="btn">Explore products</span></div>
        <div style="display:flex;gap:5px;margin-top:10px"><span class="chip"><b>Free</b> design setup</span><span class="chip"><b>Super-fast</b> delivery</span><span class="chip"><b>Free postage</b> over $400</span></div>
        <div style="margin-top:10px"><span class="chip" style="height:19px;font-size:7.5px">Call:&nbsp;<u>1300 555 014</u>&nbsp;&nbsp;•&nbsp;&nbsp;<u>Request a quote</u></span></div>
      </div>
      <div class="hero-builder">
        <div class="mock"><span class="logo">LOGO</span><span class="bar" style="top:11px;width:185px"></span><span class="bar" style="top:24px;width:235px;height:4px;background:#4a4e5c"></span></div>
        <div style="display:flex;gap:5px;margin-top:7px"><span class="chip" style="background:#3a1c24;border-color:#6a2a34">Full colour</span><span class="chip">Magnet / Pin</span><span class="chip">Domed option</span></div>
      </div>
      <div class="hero-calc">
        <div style="font-size:9.5px;font-weight:600">Calculate cost</div>
        <p class="lead" style="margin-top:5px;font-size:7.8px">Use our step-by-step Build a Badge process to get an instant online quote.</p>
        <div class="go">Start now</div>
      </div>
    </div>

    <div class="section" style="top:343px">
      <h2>Why choose us?</h2>
      <p class="lead" style="width:340px;margin-top:5px">Pinloop Cards is one of Australia's most trusted names for ID products and services.</p>
      <div class="feature-grid" style="margin-top:9px">
        <div class="feature" style="height:55px"><h4>In-depth customisation</h4><p>Choose sizes, colours, fittings and finishes to match your exact requirements.</p></div>
        <div class="feature"><h4>High-quality materials</h4><p>Durable, professional products designed for frequent use.</p></div>
        <div class="feature"><h4>Super-fast delivery</h4><p>Fast production and shipping across Australia.</p></div>
        <div class="feature"><h4>Free design setup</h4><p>We help get your artwork set up so ordering stays simple.</p></div>
        <div class="feature"><h4>Free postage</h4><p>Free delivery for badge orders over <b style="color:#fff">$400</b>.</p></div>
        <div class="feature"><h4>Australia-wide shipping</h4><p>Melbourne, Brisbane, Sydney, Adelaide, Perth, Gold Coast — everywhere.</p></div>
      </div>
    </div>

    <div class="band" style="top:535px;height:282px;background:radial-gradient(600px 200px at 30% 50%,rgba(100,30,45,.35),transparent 70%),rgba(20,22,34,.3)"></div>
    <div class="section" style="top:566px">
      <h2>Our products</h2>
      <p class="lead" style="margin-top:3px">Browse the full range — designed for businesses, events and organisations.</p>
      <div class="product-grid" style="margin-top:9px">
        <div class="product"><span class="ico" style="background:#e0a53a"></span><h4>Full colour name badges</h4><p>Professional badges with accurate full-colour logo reproduction.</p><span class="view">View</span></div>
        <div class="product"><span class="ico" style="background:#cfd2d8;border-radius:50%"></span><h4>Button badges</h4><p>Affordable promo badges for launches, trade shows and events.</p><span class="view">View</span></div>
        <div class="product"><span class="ico" style="background:#3ca35a"></span><h4>Reusable name badges</h4><p>Ideal for staff turnover, conferences and quick changes.</p><span class="view">View</span></div>
        <div class="product"><span class="ico" style="background:#d8d2b8"></span><h4>Engraved name badges</h4><p>Classic engraving for simple, elegant name and title designs.</p><span class="view">View</span></div>
        <div class="product"><span class="ico" style="background:#9aa3b5"></span><h4>Photo ID cards</h4><p>Custom photo ID cards with accessories and lanyards available.</p><span class="view">View</span></div>
        <div class="product"><span class="ico" style="background:#d8d2b8"></span><h4>Membership / Gift / Loyalty / VIP cards</h4><p>High-quality cards with optional metallic finishes.</p><span class="view">View</span></div>
        <div class="product"><span class="ico" style="background:#d8323a"></span><h4>Lapel pins</h4><p>Custom pins for awareness, achievement and unity.</p><span class="view">View</span></div>
        <div class="product"><span class="ico" style="background:#3c78d8"></span><h4>Lanyards</h4><p>Plain or printed lanyards, including popular sublimated options.</p><span class="view">View</span></div>
        <div class="product"><span class="ico" style="background:#5a6070"></span><h4 style="margin-top:4px">Animal tags</h4><p>Classic pet tags with durable enamel surface.</p><span class="view">View</span></div>
        <div class="product"><span class="ico" style="background:#5ab04a"></span><h4 style="margin-top:4px">Accessories</h4><p>Complements for your badges and ID products.</p><span class="view">View</span></div>
      </div>
    </div>

    <div class="band" style="top:817px;height:76px">
      <div class="clients"><span>Join our list of valued clients:</span><span class="list"><span class="chip">Northwire</span><span class="chip">Harbour Aid</span><span class="chip">Cresthaven</span><span class="chip">Fuelco</span><span class="chip">…</span></span></div>
    </div>

    <div class="section" style="top:923px">
      <div class="two-col">
        <div class="panel" style="height:98px"><h4>Customer testimonials</h4><p>“I thought I'd send a quick note to say thank you for the great service, I was really happy with the customer service you provided and the prompt delivery of the badge I ordered.”</p><p style="margin-top:4px"><b style="color:#fff">Rosalind</b> — Greenfield Living</p><a>Read more testimonials →</a></div>
        <div class="panel"><h4>Latest news</h4><p>When it comes to name badges, tags, and other ID products, there's no service more trusted in Australia than Pinloop Cards. Our “Build a Badge” tool lets you design your name badges online and get an instant quote.</p><span class="btn" style="margin-top:4px;height:18px">Visit blog</span></div>
      </div>
    </div>

    <div class="band" style="top:1051px;height:100px;background:rgba(18,20,30,.4)"></div>
    <div class="section" style="top:1079px">
      <div class="cta"><div class="txt"><h4>Ready to design your badges?</h4><p>It only takes a couple of minutes and provides an instant online quote.</p></div><span class="btn btn--red" style="margin-right:6px">Build a badge</span><span class="btn">Contact us</span></div>
    </div>

    <footer class="site-footer" style="height:154px">
      <div class="footer-cols">
        <div class="col" style="left:82px;top:23px"><h5>Pinloop Cards</h5>Postal: PO Box 4821, Ridgeview QLD 4399<br>Phone: 1300 555 014 &nbsp;•&nbsp; Fax: 03 5550 1234<br>© Copyright 2026. Pinloop Cards. All rights reserved.</div>
        <div class="col" style="left:425px;top:23px"><h5>Quick links</h5>Products<br>Price list<br>FAQs<br>Artwork requirements<br>Payment<br>Contact us</div>
        <div class="col" style="left:672px;top:23px"><h5>Popular products</h5>Nurse name badges<br>Identification name badges<br>Magnetic name tags<br>Plastic name badges<br>Gallery<br>Site map</div>
      </div>
    </footer>
  </section>

  <!-- Products -->
  <section class="screen screen--products">
    <div class="notice"><span class="dot"></span><span><b>Notice:</b> PC will close over Christmas / New year. We are back on <b>19th January 2025</b>.</span><span class="pay">Payment Options</span></div>
    <header class="site-header">
      <div class="brand"><i></i><span>Pinloop Cards</span></div>
      <nav class="nav"><span>Home</span><span>Products</span><span>Price list</span><span>Re-sellers / trade info</span><span>FAQs</span><span>Artwork requirements</span><span>Payment</span><span>Contact</span></nav>
      <div class="head-actions"><span class="btn">Login</span><span class="btn btn--red">Build a badge</span></div>
    </header>
    <div class="page-body" style="top:88px">
      <h3>Products</h3>
      <p class="lead" style="margin-top:4px">Choose a product category to start — then design and order online.</p>
      <div class="big-box" style="margin-top:8px;height:321px">
        <p>Categories based on the current website navigation: Full Colour Name Badges, Button Badges, Reusable Name Badges, Engraved Name Badges, Other Name Badges, Photo ID Cards, Membership / Gift / Loyalty / VIP Cards, Lapel Pins, Lanyards, Animal Tags, Accessories, Gallery.</p>
        <div class="product-grid" style="margin-top:7px">
          <div class="product"><span class="ico" style="background:#e0a53a"></span><h4>Full Colour Name Badges</h4><p>Professional badges with accurate full-colour logo reproduction.</p><span class="view">View</span></div>
          <div class="product"><span class="ico" style="background:#cfd2d8;border-radius:50%"></span><h4>Button Badges</h4><p>Affordable promo badges for launches, trade shows and events.</p><span class="view">View</span></div>
          <div class="product"><span class="ico" style="background:#3ca35a"></span><h4>Reusable Name Badges</h4><p>Highly practical for staff turnover, conferences and quick changes.</p><span class="view">View</span></div>
          <div class="product"><span class="ico" style="background:#d8d2b8"></span><h4>Engraved Name Badges</h4><p>Classic engraving for simple, elegant name and title designs.</p><span class="view">View</span></div>
          <div class="product"><span class="ico" style="background:#9aa3b5"></span><h4>Photo ID Cards</h4><p>Custom photo ID cards printed directly on durable plastic.</p><span class="view">View</span></div>
          <div class="product"><span class="ico" style="background:#d8d2b8"></span><h4>Membership / Gift / Loyalty / VIP Cards</h4><p>0.76mm thick stock with optional metallic finishes.</p><span class="view">View</span></div>
          <div class="product"><span class="ico" style="background:#d8323a"></span><h4>Lapel Pins</h4><p>Highly customisable pins for brands, charities and groups.</p><span class="view">View</span></div>
          <div class="product"><span class="ico" style="background:#3c78d8"></span><h4>Lanyards</h4><p>Plain or printed lanyards with multiple widths and options.</p><span class="view">View</span></div>
          <div class="product"><span class="ico" style="background:#5a6070"></span><h4 style="margin-top:4px">Animal Tags</h4><p>Classic pet tags with durable enamel surface.</p><span class="view">View</span></div>
          <div class="product"><span class="ico" style="background:#5ab04a"></span><h4 style="margin-top:4px">Accessories</h4><p>Badge fittings, add-ons and more.</p><span class="view">View</span></div>
          <div class="product"><span class="ico" style="background:#7ab86a"></span><h4 style="margin-top:4px">Gallery</h4><p>Product photo gallery showcasing finishes and examples.</p><span class="view">View</span></div>
        </div>
      </div>
    </div>
    <footer class="site-footer" style="height:136px">
      <div class="footer-cols">
        <div class="col" style="left:83px"><h5>Pinloop Cards</h5>Postal: PO Box 4821, Ridgeview QLD 4399<br>Phone: 1300 555 014 &nbsp;•&nbsp; Fax: 03 5550 1234<br>© Copyright 2026. Pinloop Cards. All rights reserved.</div>
        <div class="col" style="left:425px"><h5>Quick links</h5>Products<br>Price list<br>FAQs<br>Artwork requirements<br>Payment<br>Contact us</div>
        <div class="col" style="left:673px"><h5>Popular products</h5>Nurse name badges<br>Identification name badges<br>Magnetic name tags<br>Plastic name badges<br>Gallery<br>Site map</div>
      </div>
    </footer>
  </section>

  <!-- Price list -->
  <section class="screen screen--prices">
    <div class="notice"><span class="dot"></span><span><b>Notice:</b> PC will close over Christmas / New year. We are back on <b>19th January 2025</b>.</span><span class="pay">Payment Options</span></div>
    <header class="site-header">
      <div class="brand"><i></i><span>Pinloop Cards</span></div>
      <nav class="nav"><span>Home</span><span>Products</span><span>Price list</span><span>Re-sellers / trade info</span><span>FAQs</span><span>Artwork requirements</span><span>Payment</span><span>Contact</span></nav>
      <div class="head-actions"><span class="btn">Login</span><span class="btn btn--red">Build a badge</span></div>
    </header>
    <div class="page-body" style="top:88px">
      <h3>Price list</h3>
      <p class="lead" style="margin-top:4px;width:360px">This page is designed for readability. Replace the sample table with the full price table from the current site.</p>
      <div class="big-box" style="margin-top:9px">
        <p><b style="font-weight:600">FULL COLOUR NAME BADGES</b> — As at 1 July 2021<br>The prices in the table below are applicable to any of our three standard size Full Colour badges: 64mm x 19mm, 73mm x 27mm, 75mm x 25mm.<br>Prices below for standard badge backgrounds – white, metallic silver and metallic gold.<br>For Premium Backgrounds – brushed gold and silver – add $2 per badge.</p>
        <div class="note">Insert the full pricing table here (copied from the existing page), or render it server-side from your ecommerce platform.</div>
      </div>
    </div>
    <footer class="site-footer" style="height:136px">
      <div class="footer-cols">
        <div class="col" style="left:83px;top:12px"><h5>Pinloop Cards</h5>Postal: PO Box 4821, Ridgeview QLD 4399<br>Phone: 1300 555 014 &nbsp;•&nbsp; Fax: 03 5550 1234<br>© Copyright 2026. Pinloop Cards. All rights reserved.</div>
        <div class="col" style="left:425px;top:12px"><h5>Quick links</h5>Products<br>Price list<br>FAQs<br>Artwork requirements<br>Payment<br>Contact us</div>
        <div class="col" style="left:673px;top:12px"><h5>Popular products</h5>Nurse name badges<br>Identification name badges<br>Magnetic name tags<br>Plastic name badges<br>Gallery<br>Site map</div>
      </div>
    </footer>
  </section>

  <!-- Re-sellers -->
  <section class="screen screen--trade">
    <div class="notice"><span class="dot"></span><span><b>Notice:</b> PC will close over Christmas / New year. We are back on <b>19th January 2025</b>.</span><span class="pay">Payment Options</span></div>
    <header class="site-header">
      <div class="brand"><i></i><span>Pinloop Cards</span></div>
      <nav class="nav"><span>Home</span><span>Products</span><span>Price list</span><span>Re-sellers / trade info</span><span>FAQs</span><span>Artwork requirements</span><span>Payment</span><span>Contact</span></nav>
      <div class="head-actions"><span class="btn">Login</span><span class="btn btn--red">Build a badge</span></div>
    </header>
    <div class="page-body" style="top:89px">
      <h3>Re-sellers / trade info</h3>
      <p class="lead" style="margin-top:4px">Keep your existing trade copy; this page provides a clean structure.</p>
      <div class="big-box" style="margin-top:9px;height:88px">
        <p>Add the existing trade/reseller information content here (copied from the current site).</p>
        <ul><li>How to apply for trade</li><li>Trade pricing / minimum quantities</li><li>Ordering process</li><li>Contact for trade accounts</li></ul>
      </div>
    </div>
    <footer class="site-footer" style="height:136px">
      <div class="footer-cols">
        <div class="col" style="left:83px;top:15px"><h5>Pinloop Cards</h5>Postal: PO Box 4821, Ridgeview QLD 4399<br>Phone: 1300 555 014 &nbsp;•&nbsp; Fax: 03 5550 1234<br>© Copyright 2026. Pinloop Cards. All rights reserved.</div>
        <div class="col" style="left:425px;top:15px"><h5>Quick links</h5>Products<br>Price list<br>FAQs<br>Artwork requirements<br>Payment<br>Contact us</div>
        <div class="col" style="left:673px;top:15px"><h5>Popular products</h5>Nurse name badges<br>Identification name badges<br>Magnetic name tags<br>Plastic name badges<br>Gallery<br>Site map</div>
      </div>
    </footer>
  </section>

</div>
</body>
</html>
```